Brindle Financial Advice - Employer Benefit Brochure

We need to design a professional looking brochure that we can present to our existing client base, and assist in attracting new clients.
The current information is just provided in a word document, but we need to improve significantly.
The audience would be business leaders, HR decision makers and member policy committee members

Industry/Entity Type

Business

Font styles to use
Sans Serif

Colors
0255a3
f37122

```html
<!DOCTYPE html>
<html lang="en">
<head>
<meta charset="utf-8">
<title>Brindle Financial Advice – Employer Benefit Brochure</title>
<link href="https://fonts.googleapis.com/css2?family=Open+Sans:wght@400;600;700&display=swap" rel="stylesheet">
<style>
  :root {
    --band: #f7aa1f;
    --page: #ffffff;
    --ink: #1f1f1f;
    --vision-fill: #fdf4e8;
    --mission-fill: #fdf0dd;
    --value-fill: #fde5c2;
    --values-fill: #fde1b6;
  }
  html, body {
    margin: 0;
    padding: 0;
    overflow: hidden;
    background: var(--page);
  }
  .page {
    position: relative;
    width: 927px;
    height: 1200px;
    overflow: hidden;
    background: var(--page);
    font-family: "Open Sans", Arial, sans-serif;
    color: var(--ink);
  }
  .side-band {
    position: absolute;
    left: 0;
    top: 0;
    width: 105px;
    height: 100%;
    background: var(--band);
  }
  .bubble {
    position: absolute;
    border-radius: 50%;
    display: flex;
    flex-direction: column;
    align-items: center;
    justify-content: center;
    text-align: center;
    box-sizing: border-box;
  }
  .bubble h2 {
    margin: 0 0 4px;
    font-size: 16px;
    font-weight: 700;
    line-height: 1.2;
  }
  .bubble p {
    margin: 0;
    font-size: 13px;
    line-height: 1.5;
  }
  .vision {
    left: 181px; top: 203px; width: 170px; height: 170px;
    background: var(--vision-fill);
    padding: 0 14px;
  }
  .mission {
    left: 368px; top: 274px; width: 234px; height: 234px;
    background: var(--mission-fill);
    padding: 0 8px;
  }
  .mission p { font-size: 12.5px; }
  .value {
    left: 417px; top: 507px; width: 442px; height: 442px;
    background: var(--value-fill);
    padding: 80px 20px 0;
    justify-content: flex-start;
  }
  .value h2 { margin-bottom: 10px; }
  .value ul {
    list-style: none;
    margin: 0;
    padding: 0;
    white-space: nowrap;
  }
  .value li {
    font-size: 13px;
    line-height: 1.55;
    margin-bottom: 2px;
  }
  .value li::before {
    content: "•";
    margin-right: 26px;
  }
  .values {
    left: 176px; top: 866px; width: 192px; height: 192px;
    background: var(--values-fill);
    padding: 0 28px;
  }
  .intro {
    position: absolute;
    left: 134px;
    top: 404px;
    margin: 0;
    font-size: 15px;
    line-height: 24.8px;
    white-space: nowrap;
  }
  .intro .indent { padding-left: 30px; }
</style>
</head>
<body>
<main class="page">
  <div class="side-band"></div>

  <section class="bubble vision">
    <h2>Our<br>Vision</h2>
    <p>To operate a unique, superior &amp; profitable financial services business.</p>
  </section>

  <section class="bubble mission">
    <h2>Our Mission</h2>
    <p>To focus on our clients<br>and exceed their expectations<br>by providing a professional, high<br>quality client experience with the<br>emphasis on Integrated Financial<br>Services and Employer Benefit<br>Solutions for businesses,<br>individuals and families.</p>
  </section>

  <p class="intro">
    &nbsp;Brindle Financial Services<br>
    Group has been based in<br>
    North Sydney since 1983 and<br>
    has over 30 years of practical<br>
    financial planning experience.<br>
    Our long- term success has been<br>
    achieved through the building of strong<br>
    relationships and mutual trust over<br>
    many years of providing quality advice<br>
    services to our corporate and private<br>
    clients and their families.<br>
    We provide an integrated Employer<br>
    Benefits Program with solutions in<br>
    superannuation, wealth and risk<br>
    management and debt advice,<br>
    with a focus on both business<br>
    and personal financial<br>
    <span class="indent">planning.</span>
  </p>

  <section class="bubble value">
    <h2>Our Value<br>Proposition</h2>
    <ul>
      <li>We endorse the<br>employer's positioning in the benefits and<br>delivery of their Program</li>
      <li>We mitigate the legislative and<br>compliance risk with respect to superannuation</li>
      <li>We lighten the administrative burden so<br>the employer can focus on their core business</li>
      <li>We provide the employer and employee<br>with a single point of contact</li>
      <li>We bring a 'know the market' capability<br>to ensure best of breed solutions</li>
      <li>We provide a competitive<br>advantage to help attract and retain<br>the best talent</li>
    </ul>
  </section>

  <section class="bubble values">
    <h2>Our<br>Values</h2>
    <p>Honesty, Integrity, Empathy, Passion, Persistence, Accountability and Fun.</p>
  </section>
</main>
</body>
</html>
```